Business Card Design

Larkmoor Mowers was established in 1953, now under new ownership, new ownership since July 2014. We service, repair, and provide parts for all brands of outdoor power equipment. As a full service small engine repair shop we work on lawn mowers, chainsaws, weed-eaters, blowers, sprayers, pole-saws, hedge trimmers, edgers, riding mowers, zero-turn mowers, generators, and pressure washers in South Florida, Hollywood, Pembroke Pines, Miami, and surrounding areas. Catering to lawn professionals, aborists, as well as residential customers.

Larkmoor Mowers has some of the finest equipment lines you'll find in South Florida and we back our products with outstanding service, parts, friendly staff and highly trained & certified technicians. The customer is top priority when it comes to Larkmoor Mowers and we strive to provide the best possible experience when you visit our shop.

We sell also sell new commercial and residential lawn equipment including VORKA, Brisket, and KELM.

Business

Larkmoor Mowers
2846 Quillfern Ave
Hollywood FL 33857
ph: 954-555-0172
email:larkmoormowers@quillmail.example
url: www.larkmoormowers.example

```html
<!DOCTYPE html>
<html lang="en">
<head>
<meta charset="utf-8">
<title>Larkmoor Mowers – Business Card</title>
<link rel="stylesheet" href="https://fonts.googleapis.com/css2?family=Ubuntu:wght@400;500;700&display=swap">
<style>
  :root {
    --backdrop: #e9e6e1;
    --card-white: #ffffff;
    --card-black: #0b0b0b;
    --brand-green: #1fc07a;
    --brand-green-dark: #12975c;
    --ink: #1e1e1e;
    --light-text: #f2f2f2;
  }
  * { margin: 0; padding: 0; box-sizing: border-box; }
  html, body {
    width: 1200px; height: 885px; overflow: hidden;
    background: var(--backdrop);
    font-family: "Ubuntu", sans-serif;
  }
  .canvas {
    width: 1200px; height: 885px;
    display: flex; flex-direction: column;
    align-items: center; justify-content: center; gap: 60px;
  }
  .card {
    position: relative;
    width: 600px; height: 343px;
    border-radius: 3px;
    overflow: hidden;
    box-shadow: 0 10px 28px rgba(0,0,0,.22);
  }
  .card-back { background: var(--card-black); }
  .card-front { background: var(--card-white); }
  .card-shape { position: absolute; inset: 0; }

  .brand-name {
    display: flex; align-items: center; gap: 12px;
    color: var(--ink);
    font-weight: 700;
    white-space: nowrap;
  }
  .brand-mark {
    width: 16px; height: 16px;
    background: var(--brand-green);
    flex: none;
  }
  .card-back .brand-name {
    position: absolute; left: 24px; top: 150px;
    font-size: 25px;
  }
  .card-front .brand-name {
    position: absolute; left: 50%; top: 50%;
    transform: translate(-50%, -50%);
    font-size: 42px;
  }
  .card-front .brand-mark { width: 24px; height: 24px; }

  .contact {
    position: absolute; left: 338px; top: 40px;
    color: var(--light-text);
  }
  .contact .person-name {
    color: var(--brand-green);
    font-weight: 700; font-size: 24px; line-height: 1.1;
  }
  .contact .person-role {
    font-size: 15px; margin-top: 3px;
  }
  .contact .phone {
    font-size: 22px; margin-top: 40px; letter-spacing: .5px;
  }
  .contact .line {
    font-size: 12.5px; margin-top: 6px;
  }
  .contact .address { margin-top: 8px; font-size: 14px; line-height: 1.35; }
</style>
</head>
<body>
<main class="canvas">

  <section class="card card-back" aria-label="Business card, contact side">
    <svg class="card-shape" viewBox="0 0 600 343" aria-hidden="true">
      <defs>
        <linearGradient id="bandGradient" x1="0" y1="0" x2="0" y2="1">
          <stop offset="0" stop-color="var(--brand-green)"/>
          <stop offset="1" stop-color="var(--brand-green-dark)"/>
        </linearGradient>
      </defs>
      <path d="M0 0 H282 Q345 172 282 343 H0 Z" fill="url(#bandGradient)"/>
      <path d="M0 0 H268 Q331 172 268 343 H0 Z" fill="var(--card-white)"/>
    </svg>
    <div class="brand-name"><span class="brand-mark"></span>Larkmoor Mowers</div>
    <div class="contact">
      <p class="person-name">Employee Name</p>
      <p class="person-role">Managing Director</p>
      <p class="phone">954-555-0172</p>
      <p class="line">larkmoormowers@quillmail.example</p>
      <p class="line">www.larkmoormowers.example</p>
      <p class="address">2846 Quillfern Ave Hollywood<br>FL 33857</p>
    </div>
  </section>

  <section class="card card-front" aria-label="Business card, brand side">
    <div class="brand-name"><span class="brand-mark"></span>Larkmoor Mowers</div>
  </section>

</main>
</body>
</html>
```